Tech Startup Needs Business Card Design

I am looking for an eye catching business card design for our new company, Blue Kettle. We are a place for business owners and contractors to share their experiences with their customers and check their current customers. Our website, www.blue-kettle.example, may be able to offer some guidance as to the design.

Industry/Entity Type

Business

Contact Information for Business Card

Tom Varrowby
888-555-0147
Tom@blue-kettle.example
www.blue-kettle.example

```html
<!DOCTYPE html>
<html lang="en">
<head>
<meta charset="utf-8">
<title>Blue Kettle — Business Card</title>
<link rel="stylesheet" href="https://fonts.googleapis.com/css2?family=Comfortaa:wght@500;700&family=Montserrat:wght@700;800&display=swap">
<style>
  :root {
    --backdrop: #3e4040;
    --card-white: #fbfbfb;
    --card-grey: #b9bdbd;
    --brand-red: #d8141f;
    --brand-green: #1f8a3e;
    --ink: #161616;
    --url-red: #8a1f1f;
    --bubble-green: #b6d146;
    --bubble-text: #2a2a2a;
  }
  * { box-sizing: border-box; margin: 0; padding: 0; }
  html, body { width: 1200px; height: 800px; overflow: hidden; }
  body {
    background: var(--backdrop);
    font-family: "Comfortaa", sans-serif;
    display: flex;
    align-items: center;
    justify-content: center;
    gap: 40px;
  }
  .card {
    position: relative;
    width: 540px;
    height: 310px;
    border-radius: 14px;
    overflow: hidden;
  }

  /* Front */
  .card--front { background: var(--card-white); }
  .brand {
    position: absolute;
    display: flex;
    align-items: center;
    gap: 10px;
    font-family: "Comfortaa", sans-serif;
    font-weight: 700;
    color: var(--ink);
    white-space: nowrap;
  }
  .brand__dot {
    border-radius: 50%;
    background: var(--brand-red);
    flex: none;
  }
  .card--front .brand { top: 26px; left: 28px; font-size: 36px; }
  .card--front .brand__dot { width: 30px; height: 30px; }
  .holder-name {
    position: absolute;
    top: 112px;
    left: 30px;
    font-size: 27px;
    font-weight: 700;
    color: var(--brand-green);
  }
  .contact-band {
    position: absolute;
    left: 0;
    bottom: 0;
    width: 318px;
    height: 152px;
    background: var(--brand-red);
    border-top-right-radius: 34px;
    padding: 20px 14px 0 0;
    display: flex;
    flex-direction: column;
    gap: 10px;
  }
  .contact-line {
    display: flex;
    justify-content: flex-end;
    align-items: center;
    gap: 10px;
    color: #fff;
    font-size: 16px;
    font-weight: 700;
  }
  .contact-line svg { width: 26px; height: 26px; flex: none; }
  .decor-disc {
    position: absolute;
    right: -30px;
    top: 100px;
    width: 250px;
    height: 250px;
    border-radius: 50%;
    background: var(--brand-red);
  }

  /* Back */
  .card--back { background: var(--card-grey); }
  .back-panel {
    position: absolute;
    inset: 14px;
    background: var(--card-white);
    border-radius: 70px 70px 60px 60px;
  }
  .card--back .brand { top: 132px; left: 42px; font-size: 36px; }
  .card--back .brand__dot { width: 30px; height: 30px; }
  .back-url {
    position: absolute;
    top: 186px;
    left: 46px;
    font-size: 14px;
    letter-spacing: 3px;
    color: var(--url-red);
    font-weight: 500;
    white-space: nowrap;
  }
  .tagline-bubble {
    position: absolute;
    top: 30px;
    right: 26px;
    width: 238px;
    padding: 14px 14px;
    background: var(--bubble-green);
    border-radius: 22px;
    font-family: "Montserrat", sans-serif;
    font-weight: 800;
    font-size: 12px;
    line-height: 1.35;
    text-align: center;
    color: var(--bubble-text);
  }
  .tagline-bubble::after {
    content: "";
    position: absolute;
    bottom: -16px;
    left: 80px;
    border-left: 12px solid transparent;
    border-right: 12px solid transparent;
    border-top: 18px solid var(--bubble-green);
  }
  .tagline-bubble .accent-red { color: var(--brand-red); }
  .tagline-bubble .accent-green { color: var(--brand-green); }
  .mascots {
    position: absolute;
    right: 40px;
    bottom: 22px;
    width: 160px;
    height: 138px;
    border-radius: 18px;
    background: linear-gradient(135deg, #d8b79a 0%, #9a9a92 40%, #3f6ea8 70%, #c9302c 100%);
  }
</style>
</head>
<body>

  <section class="card card--front" aria-label="Business card front">
    <div class="decor-disc" aria-hidden="true"></div>
    <div class="brand"><span class="brand__dot"></span>Blue Kettle</div>
    <p class="holder-name">Tom Varrowby</p>
    <div class="contact-band">
      <p class="contact-line">888-555-0147
        <svg viewBox="0 0 26 26" aria-hidden="true"><circle cx="13" cy="13" r="11.5" fill="none" stroke="#fff" stroke-width="1.5"/><path d="M9.5 7.5l2 3-1.3 1.3c.8 1.7 2.1 3 3.8 3.8l1.3-1.3 3 2-1.3 2c-4.5-.3-8.6-4.4-8.9-8.9z" fill="#fff"/></svg>
      </p>
      <p class="contact-line">Tom@blue-kettle.example
        <svg viewBox="0 0 26 26" aria-hidden="true"><circle cx="13" cy="13" r="11.5" fill="none" stroke="#fff" stroke-width="1.5"/><rect x="7.5" y="9" width="11" height="8" fill="none" stroke="#fff" stroke-width="1.4"/><path d="M7.5 9l5.5 4.5L18.5 9" fill="none" stroke="#fff" stroke-width="1.4"/></svg>
      </p>
      <p class="contact-line">www.blue-kettle.example
        <svg viewBox="0 0 26 26" aria-hidden="true"><circle cx="13" cy="13" r="11.5" fill="none" stroke="#fff" stroke-width="1.5"/><circle cx="13" cy="13" r="6" fill="none" stroke="#fff" stroke-width="1.3"/><path d="M7 13h12M13 7c-2.5 3.5-2.5 8.5 0 12M13 7c2.5 3.5 2.5 8.5 0 12" fill="none" stroke="#fff" stroke-width="1.1"/></svg>
      </p>
    </div>
  </section>

  <section class="card card--back" aria-label="Business card back">
    <div class="back-panel"></div>
    <div class="brand"><span class="brand__dot"></span>Blue Kettle</div>
    <p class="back-url">www.blue-kettle.example</p>
    <p class="tagline-bubble">Where contractors help each other avoid <span class="accent-red">bad customers</span> &amp; only work with the <span class="accent-green">best clients!</span></p>
    <div class="mascots" role="img" aria-label="Illustration of two friendly cartoon contractors, a bearded man and a woman in overalls"></div>
  </section>

</body>
</html>
```